Website Design for Brand New Evergreen Vow Initiative

Our brand new wedding initiative works to make weddings more sustainable and help to change lives in the developing world, all while ensuring that the wedding guests have an enhanced "feel good" factor and a wedding experience like never before!

We have attached our website brief, as well as our logo, and a very short video for you to watch for some background information.

Please feel free to ask any additional questions - it's encouraged 😊

We would like this site to be completed in Wordpress, and built in a way which allows us to make future edits. Preferably using drag and drop builders.

Target Market(s)

Our target audience is couples who are in the process of planning their wedding day.
These people are in the process of deciding upon how they can make their special day stand out and be a day to remember.

They are under a lot of pressure due to the stresses of planning their special day and have a lot of factors to consider.

Industry/Entity Type

Wedding

Coding

Coded - Design and coding required

Font styles to use
Sans Serif

Requirements
Must have
• We would like this site to be completed in Wordpress, and built in a way which allows us to make future edits. Preferably using drag and drop builders.

```html
<!DOCTYPE html>
<html lang="en">
<head>
<meta charset="utf-8">
<title>Evergreen Vow Weddings</title>
<link href="https://fonts.googleapis.com/css2?family=Dancing+Script:wght@500;700&family=Lato:wght@300;400;700;900&family=Montserrat:wght@400;600;700&family=Playfair+Display:ital@1&family=Roboto:wght@400;500&display=swap" rel="stylesheet">
<style>
:root{
  --green:#2fbf0a;
  --green-bright:#35d80d;
  --green-dark:#0b7a00;
  --brand-green:#1a9c05;
  --ink:#1c1c1c;
  --body:#555;
  --white:#fff;
  --panel:rgba(52,52,52,.88);
  --slider:#555;
}
*{box-sizing:border-box;margin:0;padding:0}
html,body{width:1200px;height:2564px;overflow:hidden;background:var(--white)}
body{position:relative;font-family:"Roboto",sans-serif;color:var(--body)}
.abs{position:absolute}

/* hero */
.hero{position:absolute;left:0;top:0;width:1200px;height:642px;overflow:hidden}
.hero-photo{position:absolute;inset:0;background:linear-gradient(180deg,#3f5a2a 0%,#5e7a3c 18%,#6f7a5c 30%,#8a9293 45%,#9ea3a6 62%,#b9bcbf 80%,#c9c9cc 100%)}
.hero-photo::after{content:"";position:absolute;left:390px;top:120px;width:330px;height:522px;background:radial-gradient(ellipse at 50% 60%,rgba(235,220,225,.55),rgba(235,220,225,0) 70%)}
.brand{position:absolute;left:174px;top:28px;display:flex;align-items:center;gap:7px;font-family:"Montserrat",sans-serif;font-weight:600;font-size:12px;color:var(--white);letter-spacing:.5px}
.brand-dot{width:12px;height:12px;border-radius:50%;background:var(--white)}
.nav{position:absolute;top:34px;right:173px;display:flex;gap:25px;font-family:"Montserrat",sans-serif;font-weight:700;font-size:10.5px;color:var(--white);letter-spacing:.2px}
.hero-title{position:absolute;left:172px;top:228px;font-family:"Dancing Script",cursive;font-weight:500;font-size:56px;color:var(--white);line-height:1}
.hero-date{position:absolute;left:173px;top:293px;font-family:"Lato",sans-serif;font-size:22px;color:var(--white)}
.hero-text{position:absolute;left:174px;top:334px;width:300px;font-family:"Roboto",sans-serif;font-weight:500;font-size:13.5px;line-height:17.5px;color:var(--white)}
.get-started{position:absolute;left:669px;top:182px;width:357px;height:359px;background:var(--panel);text-align:center;padding-top:20px}
.get-started h2{font-family:"Lato",sans-serif;font-weight:900;font-size:22px;color:var(--white);letter-spacing:.3px}
.get-started p{font-family:"Lato",sans-serif;font-weight:700;font-size:15px;line-height:19px;color:var(--white);margin:8px auto 14px;width:220px}
.field{display:block;width:296px;height:30px;margin:0 auto 8px;background:var(--white);border:1px solid #ddd;font-family:"Montserrat",sans-serif;font-size:9px;color:#555;text-align:left;padding:9px 7px}
.btn-send{width:296px;height:30px;margin:0 auto;background:var(--green);font-family:"Montserrat",sans-serif;font-weight:700;font-size:9.5px;color:var(--white);line-height:30px}
.slider-ctrl{position:absolute;left:173px;top:580px;width:141px;height:62px;background:var(--slider);display:flex;align-items:center;justify-content:center;gap:12px;font-family:"Lato",sans-serif;font-size:13px;color:var(--white)}
.scroll-bump{position:absolute;left:536px;top:601px;width:130px;height:80px;border-radius:65px 65px 0 0/45px 45px 0 0;background:var(--white)}

/* sections */
.brand-mark{position:absolute;left:0;width:1200px;text-align:center;font-family:"Lato",sans-serif;font-weight:900;font-size:30px;color:var(--brand-green);letter-spacing:1px}
.script-title{position:absolute;left:0;width:1200px;text-align:center;font-family:"Dancing Script",cursive;font-weight:500;color:var(--ink);line-height:1}
.copy{position:absolute;left:350px;width:500px;text-align:center;font-size:11.5px;line-height:15px;color:var(--body)}
.btn-more{position:absolute;left:541px;top:1035px;width:118px;height:26px;background:var(--green);font-family:"Montserrat",sans-serif;font-weight:700;font-size:8px;color:var(--white);text-align:center;line-height:26px}

/* countdown */
.countdown{position:absolute;left:0;top:1121px;width:1200px;height:488px;overflow:hidden;background:linear-gradient(180deg,#4e4256 0%,#6d5a62 22%,#a47a5e 42%,#8e7566 58%,#606576 72%,#3d3a3c 88%,#2a2522 100%)}
.badge{position:absolute;left:538px;top:40px;width:124px;height:118px;border-radius:22px;background:rgba(255,255,255,.12)}
.cd-title{position:absolute;left:0;top:170px;width:1200px;text-align:center;font-family:"Dancing Script",cursive;font-weight:500;font-size:50px;color:var(--white)}
.cd-date{position:absolute;left:0;top:232px;width:1200px;text-align:center;font-family:"Lato",sans-serif;font-size:22px;color:var(--white)}
.cd-place{position:absolute;left:0;top:270px;width:1200px;text-align:center;font-family:"Playfair Display",serif;font-style:italic;font-size:32px;color:var(--white)}
.timer{position:absolute;left:0;top:345px;width:1200px;display:flex;justify-content:center;gap:38px}
.unit{width:75px;text-align:center;color:var(--white)}
.unit b{display:block;font-family:"Lato",sans-serif;font-weight:700;font-size:44px;line-height:46px}
.unit i{font-family:"Lato",sans-serif;font-size:13px}

/* details */
.subtitle{position:absolute;left:0;top:1843px;width:1200px;text-align:center;font-family:"Playfair Display",serif;font-style:italic;font-size:34px;color:var(--ink)}
.card{position:absolute;top:1999px;width:241px;height:269px;background:var(--white);box-shadow:0 1px 5px rgba(0,0,0,.18)}
.card-photo{height:174px}
.card h3{font-family:"Lato",sans-serif;font-weight:300;font-size:16px;color:#444;margin:15px 20px 14px}
.card p{font-family:"Lato",sans-serif;font-weight:300;font-size:8.5px;line-height:16px;color:#777;margin:0 20px}
.card strong{font-weight:900;color:#444}

/* footer */
.footer{position:absolute;left:0;top:2349px;width:1200px;height:215px;background:var(--green-dark);border-top:9px solid var(--green-bright);text-align:center;color:var(--white)}
.footer-brand{position:absolute;left:0;top:44px;width:1200px;font-family:"Lato",sans-serif;font-weight:900;font-size:24px;letter-spacing:1px}
.socials{position:absolute;left:557px;top:106px;display:flex;gap:5px}
.socials span{width:26px;height:26px;border-radius:50%;background:#111}
.socials span:first-child{background:var(--green-bright)}
.footer-nav{position:absolute;left:0;top:148px;width:1200px;display:flex;justify-content:center;gap:28px;font-family:"Montserrat",sans-serif;font-size:11px}
.copyright{position:absolute;left:0;top:176px;width:1200px;font-family:"Montserrat",sans-serif;font-size:8.5px}
</style>
</head>
<body>

<header class="hero">
  <div class="hero-photo" role="img" aria-label="Photo of a bride and groom embracing beside a lake with trees behind"></div>
  <div class="brand"><span class="brand-dot"></span>EVERGREEN VOW WEDDINGS</div>
  <nav class="nav"><span>HOME</span><span>ABOUT US</span><span>OUR STORY</span><span>LOCATIONS</span><span>GALLERY</span><span>CONTACT US</span></nav>
  <h1 class="hero-title">Getting Married</h1>
  <div class="hero-date">10 08 2020</div>
  <p class="hero-text">Lorem ipsum dolor sit amet, consectetur adip iscing elit, sed do eiusmod tempor incididunt ut labore et dolore magna aliqua.</p>
  <form class="get-started">
    <h2>GET STARTED</h2>
    <p>Get in touch! We can't wait to help you smile.</p>
    <span class="field">Full Name</span>
    <span class="field">Phone Number</span>
    <span class="field">Email Address</span>
    <span class="field">Wedding date</span>
    <span class="field">Number of guests</span>
    <div class="btn-send">SEND A MESSAGE</div>
  </form>
  <div class="slider-ctrl">
    <svg width="24" height="8" viewBox="0 0 24 8"><path d="M23 4H2M5 1L2 4l3 3" stroke="#fff" stroke-width="1.5" fill="none"/></svg>
    <span>1/2</span>
    <svg width="24" height="8" viewBox="0 0 24 8"><path d="M1 4h21M19 1l3 3-3 3" stroke="#fff" stroke-width="1.5" fill="none"/></svg>
  </div>
  <div class="scroll-bump">
    <svg class="abs" style="left:60px;top:14px" width="10" height="15" viewBox="0 0 10 15"><rect x="1" y="1" width="8" height="13" rx="4" stroke="#555" fill="none"/><line x1="5" y1="3.5" x2="5" y2="6" stroke="#555"/></svg>
  </div>
</header>

<section class="story">
  <div class="brand-mark" style="top:725px">EVERGREEN VOW</div>
  <h2 class="script-title" style="top:800px;font-size:66px">Our Story</h2>
  <p class="copy" style="top:897px">Morbi gravida sapien eros, vel congue felis iaculis et. Cras enim quam, rhoncus ut mi sed, cursus ultrices elit. Integer sit amet nulla non leo fringilla luctus.</p>
  <p class="copy" style="top:943px">Sed arcu sapien, pulvinar vel convallis vestibulum, dignissim non sem.Duis eu porttitor leo, sit amet viverra velit. Sed tortor neque, vehicula sit amet mattis quis, luctus eget magna. Quisque a mi ipsum.</p>
  <div class="btn-more">LEARN MORE</div>
</section>

<section class="countdown" role="img" aria-label="Photo of a city skyline at sunset under dramatic clouds">
  <div class="badge" role="img" aria-label="Hand lettered save the date badge"></div>
  <h2 class="cd-title">Wedding Sustainability</h2>
  <div class="cd-date">10 08 2020</div>
  <div class="cd-place">St. Aldric's Church,</div>
  <div class="timer">
    <div class="unit"><b>122</b><i>Hours</i></div>
    <div class="unit"><b>212</b><i>Minutes</i></div>
    <div class="unit"><b>561</b><i>Seconds</i></div>
  </div>
</section>

<section class="details">
  <div class="brand-mark" style="top:1700px">EVERGREEN VOW</div>
  <h2 class="script-title" style="top:1772px;font-size:66px">Wedding Details</h2>
  <div class="subtitle">When &amp; Where</div>
  <p class="copy" style="top:1911px">Sed arcu sapien, pulvinar vel convallis vestibulum, dignissim non sem.Duis eu porttitor leo, sit amet viverra velit. Sed tortor neque, vehicula sit amet mattis quis, luctus eget magna. Quisque a mi ipsum.</p>

  <article class="card" style="left:219px">
    <div class="card-photo" role="img" aria-label="Photo of a bride walking down the aisle at an outdoor ceremony" style="background:linear-gradient(180deg,#6f8a4a,#a8a79a 60%,#d8d6d2)"></div>
    <h3>The Venue</h3>
    <p><strong>St. Aldric's Church,</strong><br>Larkford, U.K.</p>
  </article>
  <article class="card" style="left:479px">
    <div class="card-photo" role="img" aria-label="Photo of the wedding party in suits and grey dresses holding yellow flowers" style="background:linear-gradient(180deg,#4d5a3a,#7b7866 50%,#5c5a58)"></div>
    <h3>What to Wear</h3>
    <p><strong>Keep it classy</strong>.<br>No jeans or cowboy hats please.</p>
  </article>
  <article class="card" style="left:739px">
    <div class="card-photo" role="img" aria-label="Photo of a bride and groom beside a vintage red car" style="background:linear-gradient(120deg,#8fa86a,#b9b4a4 45%,#b63a34 70%,#8c2a28)"></div>
    <h3>Parking</h3>
    <p>There is a parking lot on premises as well as down the street <strong>near the candy store</strong>.</p>
  </article>
</section>

<footer class="footer">
  <div class="footer-brand">EVERGREEN VOW</div>
  <div class="socials"><span></span><span></span><span></span></div>
  <nav class="footer-nav"><span>Home</span><span>About Us</span><span>Our Story</span><span>Locations</span><span>Gallery</span><span>Contact Us</span></nav>
  <div class="copyright">©2020 Evergreen Vow Initiative All rights reserved.</div>
</footer>

</body>
</html>
```